Wrap design for Delivery van

I need a full Body wrap for a Holtmeyer Pellio Van 2013 model.
I will showcase the brand and color (as shown in attachment) and product images and product highlight messages. It will also show the contact information and message .

the background color should be white.

Target Market(s)

Food and Beverages

Industry/Entity Type

Food and Beverages

Colors
EB3D1F
EC4F4E
F09395
F8D3D4
FCEDEE

Requirements
Must have
• Product images

```html
<!DOCTYPE html>
<html lang="en">
<head>
<meta charset="utf-8">
<title>LeafYard – Holtmeyer Pellio Van Wrap</title>
<link href="https://fonts.googleapis.com/css2?family=Poppins:wght@300;500;600&display=swap" rel="stylesheet">
<style>
  :root {
    --bg: #ffffff;
    --body: #f4f4f2;
    --body-edge: #d9d9d6;
    --window: #c9ced3;
    --green-dark: #0f7a35;
    --green-mid: #1f8a3b;
    --green-lime: #8cc63f;
    --red-deep: #b5121b;
    --red: #d71f26;
    --orange: #eb3d1f;
    --pack-red: #c8322a;
    --pack-gold: #d9a441;
    --text-green: #0f7a35;
    --text-red: #b5121b;
  }
  * { margin: 0; padding: 0; box-sizing: border-box; }
  html, body { width: 1200px; height: 1200px; overflow: hidden; background: var(--bg); }
  .wrap-sheet { width: 1200px; height: 1200px; display: flex; flex-direction: column; }
  .van-side { display: block; width: 1200px; height: 600px; }
  .van-body { fill: var(--body); stroke: var(--body-edge); stroke-width: 1.5; }
  .van-window { fill: var(--window); }
  .brand-name { font-family: "Poppins", sans-serif; font-weight: 300; font-size: 60px; fill: var(--green-dark); }
  .brand-dot { fill: var(--green-lime); }
  .social-dot { fill: var(--green-mid); }
  .contact-web { font-family: "Poppins", sans-serif; font-weight: 500; font-size: 14px; fill: var(--text-green); }
  .contact-phone { font-family: "Poppins", sans-serif; font-weight: 600; font-size: 21px; fill: var(--text-green); letter-spacing: 0.5px; }
  .contact-address { font-family: "Poppins", sans-serif; font-weight: 500; font-size: 12.5px; fill: var(--text-red); letter-spacing: 0.5px; }
  .door-line { stroke: #2b2b2b; stroke-width: 3; stroke-linecap: round; }
</style>
</head>
<body>
<main class="wrap-sheet">

  <!-- Green livery variant -->
  <svg class="van-side van-side--green" viewBox="0 0 960 480" xmlns="http://www.w3.org/2000/svg">
    <defs>
      <clipPath id="body-clip-green">
        <path d="M40,130 Q45,105 90,102 L430,100 Q470,100 520,120 L700,220 Q760,245 840,265 Q915,282 930,320 L935,405 L835,415 A72,72 0 0 0 690,415 L280,420 A72,72 0 0 0 135,420 L45,415 Z"/>
      </clipPath>
      <linearGradient id="pack-fill-green" x1="0" y1="0" x2="1" y2="1">
        <stop offset="0" stop-color="var(--pack-red)"/>
        <stop offset="1" stop-color="var(--pack-gold)"/>
      </linearGradient>
    </defs>
    <path class="van-body" d="M40,130 Q45,105 90,102 L430,100 Q470,100 520,120 L700,220 Q760,245 840,265 Q915,282 930,320 L935,405 L835,415 A72,72 0 0 0 690,415 L280,420 A72,72 0 0 0 135,420 L45,415 Z"/>
    <g clip-path="url(#body-clip-green)">
      <path fill="var(--green-dark)" d="M395,95 L960,95 L960,300 Q800,262 640,262 Q540,262 470,275 Q500,200 395,95 Z"/>
      <path fill="none" stroke="var(--green-lime)" stroke-width="9" d="M470,280 Q560,258 700,262 Q830,268 960,306"/>
      <path fill="none" stroke="var(--green-lime)" stroke-width="10" d="M385,92 Q460,150 455,270"/>
      <path fill="var(--red-deep)" d="M0,330 L300,300 L480,430 L0,430 Z"/>
      <path fill="none" stroke="var(--red)" stroke-width="14" d="M300,300 Q400,330 480,430"/>
    </g>
    <path class="van-window" d="M455,140 L640,140 Q680,145 720,225 L460,230 Z"/>
    <line class="door-line" x1="290" y1="355" x2="800" y2="355"/>
    <circle class="brand-dot" cx="262" cy="130" r="16"/>
    <text class="brand-name" x="85" y="200">LeafYard</text>
    <g class="social-links">
      <circle class="social-dot" cx="312" cy="260" r="10"/>
      <circle class="social-dot" cx="341" cy="260" r="10"/>
      <circle class="social-dot" cx="370" cy="260" r="10"/>
      <circle class="social-dot" cx="399" cy="260" r="10"/>
    </g>
    <g class="product-packs" role="img" aria-label="Product photo: three bags of plantain chips">
      <rect x="95" y="250" width="95" height="100" rx="6" fill="url(#pack-fill-green)" transform="rotate(-8 142 300)"/>
      <rect x="180" y="245" width="95" height="95" rx="6" fill="url(#pack-fill-green)" transform="rotate(-6 227 292)"/>
      <rect x="240" y="285" width="95" height="105" rx="6" fill="url(#pack-fill-green)" transform="rotate(-22 287 337)"/>
    </g>
    <text class="contact-web" x="510" y="298">www.leafyard.farm</text>
    <text class="contact-phone" x="467" y="325">+234 1 5550 0192</text>
    <text class="contact-address" x="665" y="370" text-anchor="end">House 48, Palm Crescent, Lagos,</text>
    <text class="contact-address" x="665" y="390" text-anchor="end">Nigeria 100201</text>
  </svg>

  <!-- Red livery variant -->
  <svg class="van-side van-side--red" viewBox="0 0 960 480" xmlns="http://www.w3.org/2000/svg">
    <defs>
      <clipPath id="body-clip-red">
        <path d="M40,130 Q45,105 90,102 L430,100 Q470,100 520,120 L700,220 Q760,245 840,265 Q915,282 930,320 L935,405 L835,415 A72,72 0 0 0 690,415 L280,420 A72,72 0 0 0 135,420 L45,415 Z"/>
      </clipPath>
      <linearGradient id="pack-fill-red" x1="0" y1="0" x2="1" y2="1">
        <stop offset="0" stop-color="var(--pack-red)"/>
        <stop offset="1" stop-color="var(--pack-gold)"/>
      </linearGradient>
    </defs>
    <path class="van-body" d="M40,130 Q45,105 90,102 L430,100 Q470,100 520,120 L700,220 Q760,245 840,265 Q915,282 930,320 L935,405 L835,415 A72,72 0 0 0 690,415 L280,420 A72,72 0 0 0 135,420 L45,415 Z"/>
    <g clip-path="url(#body-clip-red)">
      <path fill="var(--red)" d="M395,95 L960,95 L960,300 Q800,262 640,262 Q540,262 470,275 Q500,200 395,95 Z"/>
      <path fill="none" stroke="var(--orange)" stroke-width="9" d="M470,280 Q560,258 700,262 Q830,268 960,306"/>
      <path fill="none" stroke="var(--orange)" stroke-width="10" d="M385,92 Q460,150 455,270"/>
      <path fill="var(--red-deep)" d="M0,330 L300,300 L480,430 L0,430 Z"/>
      <path fill="none" stroke="var(--orange)" stroke-width="14" d="M300,300 Q400,330 480,430"/>
    </g>
    <path class="van-window" d="M455,140 L640,140 Q680,145 720,225 L460,230 Z"/>
    <line class="door-line" x1="290" y1="355" x2="800" y2="355"/>
    <circle class="brand-dot" cx="262" cy="130" r="16"/>
    <text class="brand-name" x="85" y="200">LeafYard</text>
    <g class="social-links">
      <circle class="social-dot" cx="312" cy="260" r="10"/>
      <circle class="social-dot" cx="341" cy="260" r="10"/>
      <circle class="social-dot" cx="370" cy="260" r="10"/>
      <circle class="social-dot" cx="399" cy="260" r="10"/>
    </g>
    <g class="product-packs" role="img" aria-label="Product photo: three bags of plantain chips">
      <rect x="95" y="250" width="95" height="100" rx="6" fill="url(#pack-fill-red)" transform="rotate(-8 142 300)"/>
      <rect x="180" y="245" width="95" height="95" rx="6" fill="url(#pack-fill-red)" transform="rotate(-6 227 292)"/>
      <rect x="240" y="285" width="95" height="105" rx="6" fill="url(#pack-fill-red)" transform="rotate(-22 287 337)"/>
    </g>
    <text class="contact-web" x="510" y="298">www.leafyard.farm</text>
    <text class="contact-phone" x="467" y="325">+234 1 5550 0192</text>
    <text class="contact-address" x="665" y="370" text-anchor="end">House 48, Palm Crescent, Lagos,</text>
    <text class="contact-address" x="665" y="390" text-anchor="end">Nigeria 100201</text>
  </svg>

</main>
</body>
</html>
```